Bourbon Lantern is a speakeasy whiskey and cigar website needing fresh look for product sales

This is a new company just starting out that will be Design needs to be modern edge of prohibition of the 1920's and the speakeasies that were created from them. Needs to include the moonshine runners, stills and whiskey. Also needs to have the sophistication of a speakeasy where gentlemen and now women go to sit in luxury leather chairs with their whiskey and cigar. Lastly my website will not be selling alcohol or cigars. Just higher end accessories and furniture designs in the Bourbon Lantern store that will help the consumer feel like they are back in time while sitting in the comfort of their own speakeasy.

I will attach my current logo but I am open to suggestions to better suit my vision. I do have photos of products that have been purchased to put on website. I am leaving the designs of actual website itself to the designer.

Target Market(s)

21 yrs +; home owners; mature audience; redesign room; cigar accessories; liquor accessories

Industry/Entity Type

home bars, liquor accessories, cigar accessories

Coding

Coded - Design and coding required

Number of Pages Required

1 page

Font styles to use
Serif
Decorative
Script

Colors

Designer to choose colors to be used in the design.

Requirements
Must have
• key words for search engines, eye catching designs matching key words, links to online store and social media
Nice to have
• logo, mixture of retro/old feel with modern day twist; speakeasy/moonshine runners with luxury and class
Should not have
• nudity, XXX, racism

```html
<!DOCTYPE html>
<html lang="en">
<head>
<meta charset="utf-8">
<title>Bourbon Lantern Store – High End Home Bar, Cigar &amp; Liquor Accessories</title>
<meta name="keywords" content="speakeasy furniture, home bar, cigar accessories, liquor accessories, whiskey decor, prohibition era, leather chairs">
<link href="https://fonts.googleapis.com/css2?family=Pinyon+Script&family=Raleway:wght@300;400;500;600;700&display=swap" rel="stylesheet">
<style>
:root{
  --tan:#b8937a;
  --tan-dark:#9c7760;
  --ink:#1d1d1d;
  --text:#6f6f6f;
  --grey-band:#ececec;
  --black:#050505;
  --white:#ffffff;
  --line:#e7c9b4;
  --mark:#2e2e2e;
}
*{box-sizing:border-box;margin:0;padding:0}
html,body{width:1200px;height:3660px;overflow:hidden}
body{position:relative;font-family:'Raleway',sans-serif;color:var(--ink);background:var(--white)}
.abs{position:absolute}
.script{font-family:'Pinyon Script',cursive;font-weight:400;color:var(--ink);white-space:nowrap}
.eyebrow{font-size:13px;letter-spacing:.5px;font-weight:500;color:var(--ink)}
.btn{position:absolute;display:flex;align-items:center;justify-content:center;background:var(--tan);color:var(--white);border-radius:20px;font-size:12px;font-weight:500;text-transform:uppercase;letter-spacing:.3px}
.photo{position:absolute}

/* header */
.site-header{position:absolute;left:0;top:0;width:1200px;height:91px;background:var(--white)}
.brand{position:absolute;left:122px;top:36px;display:flex;align-items:center;gap:8px;font-size:15px;font-weight:600;color:var(--ink)}
.brand-dot{width:14px;height:14px;border-radius:50%;background:var(--tan)}
.nav a{position:absolute;top:42px;font-size:12px;color:var(--ink);text-decoration:none}
.nav a.active{color:var(--tan)}
.phone{position:absolute;right:124px;top:61px;font-size:13px;color:#8a8a8a;display:flex;align-items:center;gap:6px}

/* hero */
.hero{position:absolute;left:0;top:91px;width:1200px;height:555px;
  background:
   radial-gradient(ellipse 90px 70px at 1020px 200px,rgba(255,214,150,.75),transparent 70%),
   radial-gradient(ellipse 200px 160px at 1050px 390px,rgba(150,70,35,.9),transparent 70%),
   radial-gradient(ellipse 150px 230px at 700px 290px,rgba(120,70,35,.9),transparent 70%),
   radial-gradient(ellipse 220px 150px at 250px 200px,rgba(140,95,65,.8),transparent 70%),
   radial-gradient(ellipse 120px 90px at 60px 470px,rgba(200,140,70,.55),transparent 70%),
   linear-gradient(180deg,#3a2519 0%,#2a1a12 60%,#1a100b 100%)}
.hero-shade{position:absolute;inset:0;background:linear-gradient(90deg,rgba(0,0,0,.45) 0%,rgba(0,0,0,.15) 55%,rgba(0,0,0,0) 100%)}
.hero-title{position:absolute;left:120px;top:232px;font-size:60px;color:var(--white)}
.hero-sub{position:absolute;left:118px;top:325px;font-size:22px;font-weight:600;color:var(--white)}
.hero-text{position:absolute;left:120px;top:368px;width:480px;font-size:18px;font-weight:300;line-height:26px;color:var(--white)}

/* about */
.about-text{position:absolute;left:121px;top:838px;width:450px;font-size:13px;font-weight:300;line-height:26px;color:var(--text)}

/* products */
.products{position:absolute;left:0;top:1193px;width:1200px;height:627px;background:var(--grey-band)}
.center{position:absolute;left:0;width:1200px;text-align:center}
.lead{font-size:13px;font-weight:300;line-height:26px}
.card{position:absolute;top:1433px;width:179px}
.card .photo{position:static;width:179px;height:179px}
.card h3{font-size:13px;font-weight:700;margin-top:10px;color:var(--ink)}
.card p{font-size:10px;line-height:17px;color:var(--text);margin-top:4px}
.go{display:inline-block;width:12px;height:12px;border-radius:50%;background:var(--tan);vertical-align:-2px;margin-left:4px;position:relative}
.go:after{content:"";position:absolute;left:3px;top:3.5px;width:4px;height:4px;border-top:1.5px solid #fff;border-right:1.5px solid #fff;transform:rotate(45deg)}

/* team */
.team{position:absolute;left:0;top:2424px;width:1200px;height:576px;
  background:
   radial-gradient(ellipse 130px 200px at 80px 330px,rgba(90,55,35,.6),transparent 70%),
   radial-gradient(ellipse 160px 200px at 1110px 330px,rgba(90,60,40,.55),transparent 70%),
   linear-gradient(90deg,#7f5a41 0%,#b18c70 30%,#b89478 60%,#8e6a50 100%)}
.member{position:absolute;top:2621px;width:246px;height:331px;background:var(--white);text-align:center}
.avatar{position:absolute;left:61px;top:40px;width:124px;height:119px;border-radius:18px;background:linear-gradient(160deg,#d9d4cf,#9f9189);border:5px solid #efefef}
.member .rule{position:absolute;top:99px;width:24px;height:2px;background:var(--ink)}
.member h4{position:absolute;left:0;top:176px;width:100%;font-size:13px;font-weight:500;color:var(--ink)}
.member .role{position:absolute;left:0;top:197px;width:100%;font-size:13px;color:var(--tan)}
.member p{position:absolute;left:26px;top:230px;width:194px;font-size:10px;line-height:13px;color:var(--text)}

/* contact */
.contact{position:absolute;left:0;top:3000px;width:1200px;height:593px;background:var(--black)}
.mark-panel{position:absolute;left:113px;top:90px;width:374px;height:375px;background:#0c0c0c}
.mark-ring{position:absolute;left:140px;top:124px;width:320px;height:320px;border-radius:50%;border:8px solid var(--mark)}
.mark-name{position:absolute;left:140px;top:265px;width:320px;text-align:center;font-size:30px;font-weight:600;color:var(--mark)}
.field{position:absolute;left:578px;width:500px;border:1px solid #5a5a5a;background:#000;font-size:10px;color:#d8d8d8;padding:10px 17px}
.footer{position:absolute;left:0;top:3593px;width:1200px;height:67px;background:var(--white);text-align:center;font-size:11px;line-height:67px;color:var(--ink)}
</style>
</head>
<body>

<header class="site-header">
  <div class="brand"><span class="brand-dot"></span>Bourbon Lantern</div>
  <nav class="nav">
    <a class="active" style="left:239px">Home</a>
    <a style="left:310px">About us</a>
    <a style="left:393px">Products</a>
    <a style="left:474px">Projects</a>
    <a style="left:551px">Our Team</a>
    <a style="left:635px">Contact Us</a>
  </nav>
  <div class="btn" style="left:956px;top:18px;width:122px;height:29px;text-transform:none;font-size:12px">Request quote</div>
  <div class="phone">
    <svg width="12" height="12" viewBox="0 0 24 24"><path fill="#b8937a" d="M6.6 10.8a15 15 0 0 0 6.6 6.6l2.2-2.2a1 1 0 0 1 1-.25 11.4 11.4 0 0 0 3.6.57 1 1 0 0 1 1 1V20a1 1 0 0 1-1 1A17 17 0 0 1 3 4a1 1 0 0 1 1-1h3.5a1 1 0 0 1 1 1c0 1.25.2 2.45.57 3.57a1 1 0 0 1-.25 1z"/></svg>
    555 0142 7788
  </div>
</header>

<section class="hero" role="img" aria-label="Friends toasting in a dim speakeasy lounge with a cigar humidor cabinet, lamp and tufted leather armchair">
  <div class="hero-shade"></div>
  <h1 class="hero-title script">Bourbon Lantern Store</h1>
  <h2 class="hero-sub">High End Accessories and Furniture Designs</h2>
  <p class="hero-text">Feels like back in time while sitting in the comfort of their own speakeasy</p>
</section>

<section class="about">
  <div class="abs eyebrow" style="left:121px;top:726px">ABOUT</div>
  <h2 class="abs script" style="left:121px;top:744px;font-size:48px">Bourbon Lantern</h2>
  <p class="about-text">Lorem ipsum dolor sit amet, consectetur adipiscing elit, sed do eiusmod tempor incididunt ut labore et dolore magna aliqua. Quis ipsum suspendisse ultrices gravida. Risus commodo viverra maecenas accumsan lacus vel facilisis.</p>
  <div class="btn" style="left:121px;top:973px;width:139px;height:35px">More info</div>
  <div class="abs" style="left:721px;top:731px;width:357px;height:329px;background:radial-gradient(circle at 70% 30%,#c9ab90,#b08f74 70%,#a4846a)"></div>
  <div class="abs" style="left:676px;top:755px;width:366px;height:367px;border:1px solid var(--line)"></div>
  <div class="photo" style="left:691px;top:771px;width:337px;height:337px;background:
    radial-gradient(ellipse 80px 140px at 290px 200px,rgba(140,120,100,.7),transparent 70%),
    radial-gradient(ellipse 110px 120px at 90px 230px,rgba(95,60,40,.9),transparent 70%),
    radial-gradient(ellipse 90px 40px at 170px 70px,rgba(120,90,60,.6),transparent 70%),
    linear-gradient(180deg,#2e241d,#1f1813 60%,#2a1c14)" role="img" aria-label="Woman in a sequined flapper dress seated beside a leather chair in a dark home bar"></div>
</section>

<section class="products">
  <div class="center eyebrow" style="top:57px">OUR</div>
  <h2 class="center script" style="top:73px;font-size:46px">Products Categories</h2>
  <p class="center lead" style="top:149px;color:var(--tan)">Lorem ipsum dolor sit amet, consectetur adipiscing elit, sed do eiusmod tempor incididunt ut labore et dolore magna<br>aliqua. Quis ipsum suspendisse ultrices gravida. Risus commodo viverra maecenas accumsan lacus vel facilisis.</p>
</section>
<svg class="abs" style="left:76px;top:1525px" width="26" height="20" viewBox="0 0 26 20"><path d="M24 10H3M11 2 3 10l8 8" fill="none" stroke="#9c7760" stroke-width="3"/></svg>
<svg class="abs" style="left:1098px;top:1525px" width="26" height="20" viewBox="0 0 26 20"><path d="M2 10h21M15 2l8 8-8 8" fill="none" stroke="#9c7760" stroke-width="3"/></svg>

<div class="card" style="left:121px"><div class="photo" style="background:radial-gradient(ellipse 60px 80px at 90px 100px,#f0dc9a,#b89448 55%,transparent 80%),linear-gradient(135deg,#cfc9bd,#8d8375 60%,#b5ada0)" role="img" aria-label="Gold cigar lighter"></div><h3>Lorem ipsum</h3><p>Lorem ipsum dolor sit amet,<br>consectetur adipiscing elit <span class="go"></span></p></div>
<div class="card" style="left:315px"><div class="photo" style="background:radial-gradient(ellipse 40px 45px at 50px 55px,#e4a060,transparent 75%),radial-gradient(ellipse 110px 45px at 100px 120px,#c06a34,transparent 75%),linear-gradient(180deg,#3a2416,#5a3018 60%,#8a4a26)" role="img" aria-label="Whiskey glass and cigar on a wooden tray"></div><h3>Mauris Auctor</h3><p>Lorem ipsum dolor sit amet,<br>consectetur adipiscing elit <span class="go"></span></p></div>
<div class="card" style="left:510px"><div class="photo" style="background:radial-gradient(ellipse 70px 90px at 110px 80px,#6b4a34,transparent 75%),radial-gradient(ellipse 50px 40px at 30px 40px,#8a7a5c,transparent 75%),linear-gradient(180deg,#3a2c22,#1e140e)" role="img" aria-label="Tufted brown leather armchair"></div><h3>Donec finibus</h3><p>Lorem ipsum dolor sit amet,<br>consectetur adipiscing elit <span class="go"></span></p></div>
<div class="card" style="left:704px"><div class="photo" style="background:radial-gradient(ellipse 45px 70px at 45px 80px,#b8c2e0,transparent 75%),radial-gradient(ellipse 55px 70px at 130px 100px,#a8b2d4,transparent 75%),linear-gradient(135deg,#0e1634,#1e2a58)" role="img" aria-label="Cut crystal whiskey glasses"></div><h3>Phasellus</h3><p>Lorem ipsum dolor sit amet,<br>consectetur adipiscing elit <span class="go"></span></p></div>
<div class="card" style="left:899px"><div class="photo" style="background:radial-gradient(ellipse 35px 70px at 90px 110px,#8a4a26,transparent 75%),radial-gradient(ellipse 50px 70px at 150px 90px,#f2f0ec,transparent 75%),linear-gradient(180deg,#6b6f6a,#d8d4cc 60%,#b8ab96)" role="img" aria-label="Wooden side table beside a cream armchair"></div><h3>Vivamus</h3><p>Lorem ipsum dolor sit amet,<br>consectetur adipiscing elit <span class="go"></span></p></div>
<div class="btn" style="left:542px;top:1714px;width:107px;height:34px">View all</div>

<section class="projects">
  <div class="abs eyebrow" style="left:126px;top:1900px">OUR</div>
  <h2 class="abs script" style="left:126px;top:1917px;font-size:46px">Recent Projects</h2>
  <p class="abs" style="left:121px;top:2014px;width:305px;font-size:13px;font-weight:300;line-height:26px;color:var(--text)">Lorem ipsum dolor sit amet, consectetur adipiscing elit, sed do eiusmod tempor incididunt ut labore et dolore magna aliqua. Quis ipsum suspendisse ultrices gravida. Risus commodo viverra maecenas accumsan lacus vel facilisis.</p>
  <div class="btn" style="left:124px;top:2194px;width:137px;height:35px">Contact us</div>
  <div class="photo" style="left:523px;top:1900px;width:269px;height:168px;background:radial-gradient(ellipse 60px 40px at 80px 120px,#b0602c,transparent 75%),radial-gradient(ellipse 60px 40px at 190px 115px,#a85a2a,transparent 75%),linear-gradient(180deg,#6a625a,#4a3e34 55%,#3a2a20)" role="img" aria-label="Leather armchairs before shelves of whiskey bottles"></div>
  <div class="photo" style="left:808px;top:1900px;width:270px;height:273px;background:radial-gradient(ellipse 60px 50px at 90px 120px,#5a8a4a,transparent 70%),radial-gradient(ellipse 70px 70px at 80px 200px,#8a5a3a,transparent 75%),radial-gradient(ellipse 70px 70px at 220px 230px,#9a6a44,transparent 75%),linear-gradient(180deg,#1e1e1c,#2a2420 60%,#4a3a30)" role="img" aria-label="Dark home bar with leather club chairs and a round wood table"></div>
  <div class="photo" style="left:523px;top:2083px;width:269px;height:273px;background:radial-gradient(ellipse 40px 30px at 140px 60px,#f0b870,transparent 75%),radial-gradient(ellipse 70px 80px at 60px 160px,#8a3e1c,transparent 75%),radial-gradient(ellipse 70px 80px at 210px 160px,#8a3e1c,transparent 75%),linear-gradient(180deg,#2a1a10,#4a2614 60%,#3a1a10)" role="img" aria-label="Pair of tufted leather chairs under a lamp in a lounge"></div>
  <div class="photo" style="left:808px;top:2188px;width:270px;height:168px;background:radial-gradient(ellipse 90px 35px at 135px 125px,#c05a24,transparent 75%),radial-gradient(ellipse 40px 30px at 60px 50px,#d88a40,transparent 75%),radial-gradient(ellipse 40px 30px at 210px 50px,#d88a40,transparent 75%),linear-gradient(180deg,#1a1412,#2e1e16 55%,#3a2216)" role="img" aria-label="Orange leather sofa set in a speakeasy lounge"></div>
</section>

<section class="team" role="img" aria-label="Warm sepia toned scene of friends laughing at a bar">
  <div class="center eyebrow" style="top:26px">OUR</div>
  <h2 class="center script" style="top:42px;font-size:46px">Team</h2>
  <p class="center lead" style="top:120px;color:var(--white)">Lorem ipsum dolor sit amet, consectetur adipiscing elit, sed do eiusmod tempor incididunt ut labore et dolore magna<br>aliqua. Quis ipsum suspendisse ultrices gravida. Risus commodo viverra maecenas accumsan lacus vel facilisis.</p>
</section>
<svg class="abs" style="left:153px;top:2729px" width="26" height="20" viewBox="0 0 26 20"><path d="M24 10H3M11 2 3 10l8 8" fill="none" stroke="#fff" stroke-width="3"/></svg>
<svg class="abs" style="left:1039px;top:2729px" width="26" height="20" viewBox="0 0 26 20"><path d="M2 10h21M15 2l8 8-8 8" fill="none" stroke="#fff" stroke-width="3"/></svg>

<div class="member" style="left:216px"><span class="rule" style="left:36px"></span><div class="avatar" style="background:linear-gradient(160deg,#e0d6cc,#a8907e)" role="img" aria-label="Team member portrait"></div><span class="rule" style="left:186px"></span><h4>Daniel R. Hayes</h4><div class="role">Furniture Designer</div><p>Lorem ipsum dolor sit amet, consectetur adipiscing elit, sed do eiusmod tempor incididunt ut labore et dolore magna aliqua. Quis ipsum suspendisse ultrices gravida.</p></div>
<div class="member" style="left:487px"><span class="rule" style="left:36px"></span><div class="avatar" style="background:linear-gradient(160deg,#3a3836,#b89a86 60%,#6a6460)" role="img" aria-label="Team member portrait"></div><span class="rule" style="left:186px"></span><h4>Daniel R. Hayes</h4><div class="role">Furniture Designer</div><p>Lorem ipsum dolor sit amet, consectetur adipiscing elit, sed do eiusmod tempor incididunt ut labore et dolore magna aliqua. Quis ipsum suspendisse ultrices gravida.</p></div>
<div class="member" style="left:758px"><span class="rule" style="left:36px"></span><div class="avatar" style="background:linear-gradient(160deg,#9ab0c0,#c89478 55%,#4a5a6a)" role="img" aria-label="Team member portrait"></div><span class="rule" style="left:186px"></span><h4>Daniel R. Hayes</h4><div class="role">Furniture Designer</div><p>Lorem ipsum dolor sit amet, consectetur adipiscing elit, sed do eiusmod tempor incididunt ut labore et dolore magna aliqua. Quis ipsum suspendisse ultrices gravida.</p></div>

<section class="contact">
  <div class="mark-panel"></div>
  <div class="mark-ring"></div>
  <div class="mark-name">Bourbon Lantern</div>
  <h2 class="abs script" style="left:577px;top:80px;font-size:44px;color:var(--white)">Contact us</h2>
  <p class="abs" style="left:577px;top:136px;width:480px;font-size:13px;font-weight:300;line-height:26px;color:var(--tan)">Lorem ipsum dolor sit amet, consectetur adipiscing elit, sed do eiusmod tempor incididunt ut labore et dolore magna aliqua.</p>
</section>
<div class="field" style="top:3209px;height:33px">Full Name</div>
<div class="field" style="top:3263px;height:31px">Your Email Address</div>
<div class="field" style="top:3317px;height:98px">Your Message</div>
<div class="btn" style="left:577px;top:3436px;width:109px;height:36px">Submit</div>

<footer class="footer">Copyright 2024 bourbonlantern.com All Rights Reserved.</footer>

</body>
</html>
```